Web Design Project for Web Agency

WHAT I NEED:
The design I need (PSD file) is for a microsite designed for employee recruitment for Brennick, a Web agency.
***Design for the 1st Page ONLY : "Manifeste"
OBJECTIVES OF THE WEBSITE:
1. To promote the agency's corporate culture and HR management principles.
2. To get people to apply on available jobs
ELEMENTS OF THE PAGE "MANIFESTE" :
1. Brennick logo (see attached files). Beside the logo must be the word "Carrières" ("Careers" in english)
***The logo is not final and there is NO branding for Brennick yet. That is why there are multiple files. So please feel free to be creative!
2. Main menu : 4 sections
Manifeste | Opportunités | Brenick | Postuler
3. Manifeste :
This page is the home page. It will present 2 main sections :
a. The agency's corporate culture :
- Title of the page is a question : "Do you embrace Brennick's corporate culture?"
- Then, presentation of the 5 corporate values, each with a title and short description
- At the end of the list of values, we want a button that says "Apply now"
b. The agency's HR management principles :
- Title of the page is a question : "Do you see yourself working at Brennick?"
- Then, presentation of the 5 Management principles, each with a title and short description
- At the end of the list of principles, we want a button that says "Apply now"
VISUAL INSPIRATION
To create each section of the "Manifeste" page, we want a design that will fit with the corporate culture:
- Brennick is BOLD
- Brennick is PROUD
- Brennick is PROFESSIONAL
- Brennick is ELEGANT
- Brennick is REFINED
We want something slick and modern. Here are some Website's that we like that can be of inspiration:
- http://www.studio-varnel.com/en/services
- http://quillmorrowlab.com/

```html
<!DOCTYPE html>
<html lang="fr">
<head>
<meta charset="utf-8">
<title>Brennick — Carrières — Manifeste</title>
<link rel="stylesheet" href="https://fonts.googleapis.com/css2?family=Archivo:wght@400;600;700&family=Archivo+Black&display=swap">
<style>
  :root {
    --paper: #f4f3f2;
    --ink: #000000;
    --white: #ffffff;
    --orange: #f07a3c;
    --orange-deep: #e8621f;
    --orange-photo-a: #f3873f;
    --orange-photo-b: #c2461a;
    --grey-text: #8a8a8a;
    --footer-band: #ebebeb;
    --shadow: #e6e5e4;
    --glow: #e0463a;
  }
  * { box-sizing: border-box; margin: 0; padding: 0; }
  html, body { width: 961px; height: 1200px; overflow: hidden; }
  body {
    position: relative;
    background: var(--paper);
    font-family: "Archivo", Arial, sans-serif;
    color: var(--ink);
  }
  .abs { position: absolute; }

  /* top navigation */
  .topbar { left: 0; top: 0; width: 961px; height: 34px; }
  .main-nav { top: 11px; left: 476px; display: flex; gap: 0; font-size: 11px; color: var(--white); }
  .main-nav a { position: absolute; color: var(--white); text-decoration: none; white-space: nowrap; }
  .social { top: 11px; left: 781px; display: flex; gap: 11px; }
  .social span { width: 11px; height: 11px; border-radius: 50%; background: var(--white); display: block; }

  /* hero */
  .hero-photo { left: 0; top: 0; width: 961px; height: 530px; }
  .brand { left: 97px; top: 62px; text-align: center; }
  .brand-name { font-family: "Archivo", Arial, sans-serif; font-weight: 600; font-size: 31px; letter-spacing: 0.5px; line-height: 1; }
  .brand-sub { font-size: 11px; letter-spacing: 2.4px; margin-top: 7px; }
  .careers { left: 123px; top: 161px; font-size: 14px; display: flex; align-items: center; gap: 14px; }
  .careers-arrow { width: 20px; height: 11px; background: var(--ink); display: flex; align-items: center; justify-content: center; }

  .hero-lead {
    left: 180px; top: 207px; width: 600px; text-align: center;
    color: var(--white); text-transform: uppercase;
    font-size: 22px; line-height: 22px; letter-spacing: 0.6px;
  }
  .hero-lead b { font-family: "Archivo Black", Arial, sans-serif; font-weight: 400; letter-spacing: 1.5px; }
  .btn-hero {
    left: 369px; top: 295px; width: 194px; height: 34px;
    background: var(--ink); color: var(--white); border-radius: 5px;
    box-shadow: 0 0 0 3px var(--glow), 0 0 6px 3px rgba(224,70,58,.5);
    font-weight: 700; font-size: 14px; letter-spacing: .5px;
    display: flex; align-items: center; justify-content: center;
  }

  /* sections */
  .section-title {
    left: 0; width: 961px; text-align: center;
    font-family: "Archivo Black", Arial, sans-serif; font-weight: 400;
    color: var(--orange-deep); font-size: 18.5px; letter-spacing: 2px;
  }
  .value { width: 124px; height: 140px; }
  .value svg { display: block; }
  .value-shadow { position: absolute; left: 30px; top: 143px; width: 64px; height: 18px; border-radius: 50%; background: var(--shadow); }
  .value-label { position: absolute; left: 0; top: 64px; width: 124px; text-align: center; font-size: 10px; color: var(--white); }
  .value-note { left: 380px; top: 697px; width: 200px; text-align: center; font-size: 9.5px; line-height: 11px; color: var(--grey-text); }
  .btn-apply {
    left: 386px; width: 190px; height: 31px;
    background: var(--orange); color: var(--white); border-radius: 5px;
    box-shadow: 0 0 0 3px rgba(240,122,60,.18);
    font-size: 14px; letter-spacing: .8px;
    display: flex; align-items: center; justify-content: center;
  }

  /* footer */
  .to-top { left: 781px; top: 1080px; width: 62px; height: 32px; border-radius: 31px 31px 0 0; background: var(--ink); display: flex; justify-content: center; padding-top: 8px; }
  .footer-links { left: 0; top: 1112px; width: 961px; height: 45px; background: var(--footer-band); display: flex; justify-content: center; align-items: center; font-size: 10px; gap: 6px; }
  .footer-bottom { left: 0; top: 1157px; width: 961px; height: 43px; }
  .copyright { left: 98px; top: 1172px; font-size: 9.5px; color: var(--white); }
  .footer-brand { left: 763px; top: 1165px; text-align: center; }
  .footer-brand .brand-name { font-size: 20px; }
  .footer-brand .brand-sub { font-size: 7px; letter-spacing: 1.6px; margin-top: 3px; }
</style>
</head>
<body>

<svg width="0" height="0" style="position:absolute" aria-hidden="true">
  <defs>
    <linearGradient id="photoTone" x1="0" y1="0" x2="1" y2="1">
      <stop offset="0" stop-color="#f59a55"/>
      <stop offset=".5" stop-color="#ee6f2c"/>
      <stop offset="1" stop-color="#b6421a"/>
    </linearGradient>
    <symbol id="icon-pen" viewBox="0 0 32 32"><path d="M6 26 L24 8 L27 11 L9 29 L5 30 Z" fill="#fff"/><rect x="4" y="30" width="24" height="1.5" fill="#fff"/></symbol>
    <symbol id="icon-cup" viewBox="0 0 32 32"><path d="M6 12 H22 V24 Q22 28 18 28 H10 Q6 28 6 24 Z" fill="#fff"/><path d="M22 15 Q28 15 28 19 Q28 23 22 23" stroke="#fff" stroke-width="2.4" fill="none"/><rect x="4" y="30" width="22" height="1.5" fill="#fff"/><path d="M14 3 Q12 6 14 9" stroke="#fff" stroke-width="1.3" fill="none"/></symbol>
    <symbol id="icon-chair" viewBox="0 0 32 32"><rect x="9" y="3" width="14" height="12" rx="3" fill="#fff"/><rect x="5" y="15" width="22" height="4" rx="2" fill="#fff"/><rect x="15" y="19" width="2" height="6" fill="#fff"/><path d="M7 29 L16 25 L25 29" stroke="#fff" stroke-width="2" fill="none"/></symbol>
    <symbol id="icon-people" viewBox="0 0 32 32"><circle cx="10" cy="6" r="4" fill="#fff"/><circle cx="22" cy="6" r="4" fill="#fff"/><rect x="5" y="11" width="10" height="12" rx="3" fill="#fff"/><rect x="17" y="11" width="10" height="12" rx="3" fill="#fff"/><rect x="7" y="22" width="6" height="9" fill="#fff"/><rect x="19" y="22" width="6" height="9" fill="#fff"/></symbol>
    <symbol id="icon-plane" viewBox="0 0 32 32"><path d="M2 14 L30 4 L20 26 L15 18 Z" fill="#fff"/><path d="M15 18 L12 26 L17 21" fill="#fff"/><path d="M2 30 Q6 22 12 22" stroke="#fff" stroke-width="1.2" fill="none"/></symbol>
  </defs>
</svg>

<!-- hero band with photograph area -->
<svg class="abs hero-photo" width="961" height="530" viewBox="0 0 961 530">
  <polygon points="397,34 961,34 961,229 0,523 0,427" fill="url(#photoTone)" role="img" aria-label="Photograph of smiling colleagues working together at a computer, tinted orange"/>
</svg>

<!-- top bar -->
<svg class="abs topbar" width="961" height="34" viewBox="0 0 961 34" aria-hidden="true">
  <polygon points="432,0 961,0 961,34 395,34" fill="var(--ink)"/>
</svg>
<nav class="abs main-nav">
  <a style="left:0">Manifeste</a>
  <a style="left:67px">Opportunités</a>
  <a style="left:150px">Brenick</a>
  <a style="left:207px">Postuler</a>
</nav>
<div class="abs social" aria-label="Social links"><span></span><span></span><span></span><span></span></div>

<header class="abs brand">
  <div class="brand-name">Brennick</div>
  <div class="brand-sub">agence numérique</div>
</header>
<div class="abs careers">Carrières
  <span class="careers-arrow"><svg width="12" height="8" viewBox="0 0 12 8"><path d="M0 4 H10 M7 1 L10 4 L7 7" stroke="#fff" stroke-width="1.6" fill="none"/></svg></span>
</div>

<h1 class="abs hero-lead" style="font-weight:400"><b>Brennick</b> sem non augue posuere,<br>pharetra <b>suscipit</b> urna mattis.<br><b>Ante</b> ipsum primis</h1>
<a class="abs btn-hero">APPLY NOW!</a>

<!-- corporate culture -->
<h2 class="abs section-title" style="top:485px">DO YOU EMBRACE BRENNICK'S CORPORATE CULTURE?</h2>

<div class="abs value" style="left:97px;top:531px"><svg width="124" height="124"><polygon points="62,0 124,62 62,124 0,62" fill="var(--ink)"/><use href="#icon-pen" x="50" y="38" width="26" height="26"/></svg><span class="value-label">Consectetur</span><span class="value-shadow"></span></div>
<div class="abs value" style="left:258px;top:531px"><svg width="124" height="124"><polygon points="62,0 124,62 62,124 0,62" fill="var(--ink)"/><use href="#icon-cup" x="50" y="34" width="28" height="28"/></svg><span class="value-label">Consectetur</span><span class="value-shadow"></span></div>
<div class="abs value" style="left:419px;top:531px"><svg width="124" height="124"><polygon points="62,0 124,62 62,124 0,62" fill="var(--orange)"/><use href="#icon-chair" x="48" y="34" width="28" height="28"/></svg><span class="value-label">Consectetur</span><span class="value-shadow"></span></div>
<div class="abs value" style="left:583px;top:531px"><svg width="124" height="124"><polygon points="62,0 124,62 62,124 0,62" fill="var(--ink)"/><use href="#icon-people" x="49" y="34" width="28" height="28"/></svg><span class="value-label">Consectetur</span><span class="value-shadow"></span></div>
<div class="abs value" style="left:741px;top:531px"><svg width="124" height="124"><polygon points="62,0 124,62 62,124 0,62" fill="var(--ink)"/><use href="#icon-plane" x="48" y="34" width="30" height="30"/></svg><span class="value-label">Consectetur</span><span class="value-shadow"></span></div>

<p class="abs value-note">Lorem ipsum dolor sit<br>adipiscing elit. Ut vulputate</p>
<a class="abs btn-apply" style="top:735px">APPLY NOW!</a>

<!-- management principles -->
<h2 class="abs section-title" style="top:801px">DO YOU SEE YOURSELF WORKING AT BRENNICK?</h2>

<div class="abs value" style="left:97px;top:847px"><svg width="124" height="124"><polygon points="62,0 124,62 62,124 0,62" fill="var(--ink)"/><use href="#icon-pen" x="50" y="38" width="26" height="26"/></svg><span class="value-label">Consectetur</span><span class="value-shadow"></span></div>
<div class="abs value" style="left:258px;top:847px"><svg width="124" height="124"><polygon points="62,0 124,62 62,124 0,62" fill="var(--ink)"/><use href="#icon-cup" x="50" y="34" width="28" height="28"/></svg><span class="value-label">Consectetur</span><span class="value-shadow"></span></div>
<div class="abs value" style="left:419px;top:847px"><svg width="124" height="124"><polygon points="62,0 124,62 62,124 0,62" fill="var(--ink)"/><use href="#icon-chair" x="48" y="34" width="28" height="28"/></svg><span class="value-label">Consectetur</span><span class="value-shadow"></span></div>
<div class="abs value" style="left:583px;top:847px"><svg width="124" height="124"><polygon points="62,0 124,62 62,124 0,62" fill="var(--ink)"/><use href="#icon-people" x="49" y="34" width="28" height="28"/></svg><span class="value-label">Consectetur</span><span class="value-shadow"></span></div>
<div class="abs value" style="left:741px;top:847px"><svg width="124" height="124"><polygon points="62,0 124,62 62,124 0,62" fill="var(--ink)"/><use href="#icon-plane" x="48" y="34" width="30" height="30"/></svg><span class="value-label">Consectetur</span><span class="value-shadow"></span></div>

<a class="abs btn-apply" style="top:1046px">APPLY NOW!</a>

<!-- footer -->
<a class="abs to-top" aria-label="Back to top"><svg width="10" height="10" viewBox="0 0 10 10"><path d="M5 9 V2 M2 5 L5 2 L8 5" stroke="#fff" stroke-width="1.6" fill="none"/></svg></a>
<nav class="abs footer-links"><span>Manifeste</span>|<span>Opportunités</span>|<span>Brennick</span>|<span>Postuler</span></nav>
<svg class="abs footer-bottom" width="961" height="43" viewBox="0 0 961 43" aria-hidden="true">
  <polygon points="0,0 540,0 577,43 0,43" fill="var(--ink)"/>
</svg>
<p class="abs copyright">Copyright © Brennick Agence Nunerique</p>
<div class="abs brand footer-brand">
  <div class="brand-name">Brennick</div>
  <div class="brand-sub">agence numérique</div>
</div>

</body>
</html>
```